Marisol Lodge website redesign

After 8 years of our current site, we're ready to upgrade our site design. We'd like to generally make it more modern and clean and build it on a CMS like joomla for easier future maintenance.

Our hotel is a family-owned bed and breakfast that competes against much larger hotel chains in Aspen with fancier rooms and larger pricetags. Our hotel is priced moderately and features tasteful, uniquely-design rooms.

We are looking for a website that will showcase the uniqueness of our rooms, the history of the Lodge, and the friendliness of our staff.

Here are some other hotel sites we like:

http://www.thecopperwren.example/

http://www.pinecrestridgehouse.example/

http://www.hotelbrivaro.example/

*********

Scope of Work - I'm looking for a design AND build. The website should be built out in Joomla as part of the final deliverable.

Current website: http://www.marisollodge.example/

Explanation of what design + build means:

I am looking for not only the design of the site, but also for the homepage and one subpage to be built out as well. I do NOT need the entire site built - only for those two pages to be built and I will retrofit the remainder of the pages.

Target Market(s)

travellers evaluating hotels in Aspen, Colorado.

Industry/Entity Type

Hotel

Requirements
Must have
• Must, must, must be based on a joomla template. "Rotating" large main image as central position on homepage is a must (see example websites mentioned above).

Nice to have
• We have an existing online reservation system. It would be nice to evaluate placing a "widget" on the homepage that integrates to the online reservation page. Similar to that feature that the Copper Wren website has at the foot of the main image on their homepage.

```html
<!DOCTYPE html>
<html lang="en">
<head>
<meta charset="utf-8">
<title>Marisol Lodge</title>
<link href="https://fonts.googleapis.com/css2?family=Great+Vibes&family=Arimo:wght@400&family=Noto+Serif:ital@0;1&display=swap" rel="stylesheet">
<style>
:root{
  --page:#e9e8e6;
  --band:#dddcda;
  --accent:#8c3a2b;
  --accent-soft:#c99a8e;
  --text:#3f3f3f;
  --field-border:#d6a89d;
  --white:#ffffff;
  --footer:#f7f7f7;
}
*{margin:0;padding:0;box-sizing:border-box}
html,body{width:917px;height:1200px;overflow:hidden}
body{position:relative;background:var(--page);font-family:"Arimo",Arial,sans-serif;color:var(--text)}
.abs{position:absolute}
.script{font-family:"Great Vibes",cursive;color:var(--accent);word-spacing:3px}
.brand{left:0;width:917px;top:30px;text-align:center;font-size:44px;line-height:1}
.ornament{top:46px;width:64px;height:28px;background:linear-gradient(#d8d7d5,#cfcecc);border-radius:14px;opacity:.8}
.nav{left:0;top:112px;width:917px;height:42px;background:var(--band);border-top:1px solid var(--accent-soft);border-bottom:1px solid #c9c8c6}
.nav a{position:absolute;top:11px;font-size:16px;text-decoration:none;white-space:nowrap}
.hero{left:70px;top:172px;width:778px;height:365px;background:var(--white);box-shadow:0 2px 6px rgba(0,0,0,.25)}
.hero-photo{left:7px;top:7px;width:763px;height:350px;background:linear-gradient(120deg,#f3ece8 0%,#e7d3cb 40%,#c9a89d 60%,#f1e9e5 100%)}
.hero-caption{left:7px;top:296px;width:763px;height:61px;background:rgba(140,58,43,.72)}
.hero-caption span{position:absolute;left:21px;top:16px;font-family:"Great Vibes",cursive;color:var(--white);font-size:24px;word-spacing:2px}
.heading{font-size:24px;line-height:1;white-space:nowrap}
.label{font-size:10.5px;line-height:13px}
.select{height:15px;background:var(--white);border:1px solid var(--field-border);font-size:10px;padding-left:6px;line-height:13px}
.select::after{content:"";position:absolute;right:0;top:0;width:13px;height:13px;background:#9c9c9c}
.select::before{content:"";position:absolute;right:3px;top:5px;border:3.5px solid transparent;border-top:4px solid #222;z-index:1}
.input{height:15px;background:var(--white);border:1px solid var(--field-border)}
.btn{height:35px;background:var(--band);border-top:1px solid var(--accent-soft);border-bottom:1px solid #c9c8c6;text-align:center;font-size:18px;line-height:33px}
.rule{height:1px;background:var(--accent-soft)}
.rule.grey{background:#9a9a9a}
.body-copy{font-size:10.4px;line-height:13px;width:385px}
.quote{font-family:"Noto Serif",serif;font-style:italic;font-size:9px;line-height:18.7px;width:300px}
.quote-by{font-family:"Noto Serif",serif;font-size:10.5px}
.video{left:447px;top:805px;width:274px;height:170px;border:1px solid #444;background:linear-gradient(180deg,#e6e6e6 0%,#b9a996 45%,#6b4a34 75%,#3e3a34 100%)}
.video-bar{left:0;bottom:0;width:100%;height:13px;background:#1c1c1c}
.thumb{left:747px;width:78px;height:48px;border:1px solid #444;background:linear-gradient(180deg,#e3e3e3,#8a6a50 70%,#2b2b2b);box-shadow:2px 2px 3px rgba(0,0,0,.35)}
.footer{left:0;top:1043px;width:917px;height:119px;background:var(--band);border-top:1px solid #b9b8b6;border-bottom:1px solid var(--accent-soft)}
.small{font-size:9.5px;line-height:12px}
.social{top:1083px;width:14px;height:14px;border-radius:50%;background:var(--accent)}
.badge{background:#f4f4f2;border:1px solid #cfcfcf}
.legal{left:0;top:1165px;width:917px;height:35px;background:var(--footer)}
.legal span{position:absolute;left:70px;top:13px;font-size:9px}
</style>
</head>
<body>

<div class="abs ornament" role="img" aria-label="Decorative flourish" style="left:228px"></div>
<div class="abs script brand">Marisol Lodge</div>
<div class="abs ornament" role="img" aria-label="Decorative flourish" style="left:624px"></div>

<nav class="abs nav script">
  <a style="left:83px">About The Lodge</a>
  <a style="left:211px">Rooms</a>
  <a style="left:288px">Amenities</a>
  <a style="left:379px">Aspen Information</a>
  <a style="left:526px">Managers Journal</a>
  <a style="left:671px">Web Cam's</a>
  <a style="left:769px">Contact Us</a>
</nav>

<section class="abs hero">
  <div class="abs hero-photo" role="img" aria-label="Rotating photo of a lodge sitting room with white chairs, red toile cushions, orchids and glass lanterns"></div>
  <div class="abs hero-caption"><span>Stay 3 nights, get the 4th night FREE!!!</span></div>
</section>

<div class="abs script heading" style="left:74px;top:572px">Online Booking</div>
<div class="abs label" style="left:74px;top:615px">Check In :</div>
<div class="abs select" style="left:136px;top:614px;width:79px">Date :</div>
<div class="abs label" style="left:225px;top:615px">Check Out :</div>
<div class="abs select" style="left:289px;top:614px;width:79px">Date :</div>
<div class="abs label" style="left:74px;top:647px">Number<br>of Persons :</div>
<div class="abs select" style="left:136px;top:651px;width:61px">2</div>
<div class="abs label" style="left:225px;top:647px">Number<br>of Rooms :</div>
<div class="abs select" style="left:289px;top:651px;width:61px">1</div>
<div class="abs label" style="left:74px;top:689px">Your Name :</div>
<div class="abs input" style="left:143px;top:687px;width:135px"></div>
<div class="abs label" style="left:74px;top:726px">Phone :</div>
<div class="abs input" style="left:143px;top:723px;width:135px"></div>
<div class="abs label" style="left:74px;top:760px">Email :</div>
<div class="abs input" style="left:143px;top:760px;width:135px"></div>
<div class="abs btn script" style="left:74px;top:794px;width:85px">Book Now</div>
<div class="abs rule" style="left:70px;top:845px;width:303px"></div>

<div class="abs script heading" style="left:73px;top:865px">Testimonials</div>
<p class="abs quote" style="left:74px;top:895px">This lodge is located right on Main Street. The innkeeper and owner are so friendly, and they recommended places for us to eat within walking distance and places to drive to see the changing aspens.</p>
<div class="abs quote-by" style="left:74px;top:958px">- Dana Hollis, <i>Fernbrook, Colorado</i></div>
<div class="abs btn script" style="left:74px;top:990px;width:85px">More...</div>

<div class="abs script heading" style="left:442px;top:572px">Welcome to the Marisol Lodge</div>
<p class="abs body-copy" style="left:443px;top:609px">Located in the heart of downtown Aspen, the newly renovated Marisol Lodge possesses all the charms of a vintage European Ski Lodge, while offering all of the modern conveniences one would expect with a stay in Aspen.</p>
<p class="abs body-copy" style="left:443px;top:665px">A stay at our lodge includes free continental breakfast in our dining room, daily maid service, free wireless internet access, and a fully-equipped conference facility. Guests are also invited to relax in one of our two outdoor hot tubs or in our lounge, where a 42-inch plasma TV and fireplace make for a pleasant area to unwind.</p>
<div class="abs rule grey" style="left:442px;top:741px;width:406px"></div>

<div class="abs script heading" style="left:445px;top:767px">Click here for a virtual tour of the lodge!</div>
<div class="abs video" role="img" aria-label="Video tour of the lodge exterior in winter with clock tower">
  <svg class="abs" style="left:120px;top:65px" width="36" height="36" viewBox="0 0 36 36"><circle cx="18" cy="18" r="17" fill="rgba(0,0,0,.45)"/><path d="M14 11 L26 18 L14 25 Z" fill="#fff" opacity=".85"/></svg>
  <div class="abs video-bar"></div>
</div>
<div class="abs thumb" style="top:806px" role="img" aria-label="Lodge exterior video thumbnail"></div>
<div class="abs thumb" style="top:866px" role="img" aria-label="Lodge exterior video thumbnail"></div>
<div class="abs thumb" style="top:925px" role="img" aria-label="Lodge exterior video thumbnail"></div>
<div class="abs btn script" style="left:450px;top:990px;width:85px">More...</div>

<footer class="abs footer"></footer>
<div class="abs script heading" style="left:79px;top:1054px;font-size:21px">The Marisol Lodge</div>
<div class="abs small" style="left:83px;top:1085px">418 Larkspur Avenue</div>
<div class="abs small" style="left:83px;top:1103px">Aspen, CO 81699</div>

<div class="abs script heading" style="left:386px;top:1054px;font-size:21px">Follow Us On</div>
<div class="abs social" style="left:386px"></div>
<div class="abs social" style="left:406px"></div>
<div class="abs social" style="left:426px"></div>
<div class="abs social" style="left:446px"></div>
<div class="abs social" style="left:466px"></div>

<svg class="abs" style="left:387px;top:1120px" width="9" height="12" viewBox="0 0 9 12"><rect x="1" y="0.5" width="7" height="11" rx="1.2" fill="none" stroke="var(--accent)" stroke-width="1.2"/><circle cx="4.5" cy="9.3" r=".8" fill="var(--accent)"/></svg>
<div class="abs small" style="left:410px;top:1121px">800-555-0147 / 970-555-0182</div>
<svg class="abs" style="left:386px;top:1143px" width="12" height="9" viewBox="0 0 12 9"><rect x=".5" y=".5" width="11" height="8" fill="none" stroke="var(--accent)"/><path d="M.5 .5 L6 5 L11.5 .5 M.5 8.5 L4.5 4 M11.5 8.5 L7.5 4" fill="none" stroke="var(--accent)"/></svg>
<div class="abs small" style="left:410px;top:1142px">info@marisollodge.example</div>

<div class="abs script heading" style="left:708px;top:1054px;font-size:21px">Trusted By</div>
<div class="abs badge" style="left:708px;top:1087px;width:65px;height:53px"></div>
<div class="abs badge" style="left:791px;top:1087px;width:42px;height:69px;background:#dfe8d6"></div>

<div class="abs legal"><span>© 2012 Marisol Lodge</span></div>

</body>
</html>
```